Business Card Design

We just need these details on one side of card and logo on the other.

Industry/Entity Type

Business

Contact Information for Business Card

Lisel Pardoe | Artist
118 Coldwell Street
Malvern East Vic 3145
# 0412 978 205 | 03 9187 2604
lisel@liselpardoe.com
liselsnook.com.au

```html
<!DOCTYPE html>
<html lang="en">
<head>
<meta charset="utf-8">
<title>Lisel Pardoe – Business Card</title>
<link rel="stylesheet" href="https://fonts.googleapis.com/css2?family=Marcellus+SC&display=swap">
<style>
  :root {
    --backdrop: #e9e6e1;
    --card-white: #fbfbf9;
    --card-black: #0e0e0e;
    --ink: #1c1c1c;
    --ink-soft: #3a3a3a;
    --silver: #c9c9c9;
    --silver-dim: #7a7a7a;
  }
  * { box-sizing: border-box; margin: 0; padding: 0; }
  html, body {
    width: 924px; height: 1200px; overflow: hidden;
    background: var(--backdrop);
  }
  body {
    font-family: "Marcellus SC", "Copperplate", serif;
    display: flex; flex-direction: column; align-items: center; justify-content: center;
    gap: 70px;
  }
  .card {
    width: 770px; height: 440px;
    position: relative;
    box-shadow: 0 6px 18px rgba(0,0,0,0.18);
  }

  /* Contact side */
  .card--contact { background: var(--card-white); color: var(--ink); }
  .identity {
    position: absolute; top: 44px; right: 80px;
    text-align: center;
  }
  .identity__first {
    font-size: 60px; letter-spacing: 2px; line-height: 1; color: var(--ink);
  }
  .identity__last {
    margin-top: 4px; font-size: 22px; letter-spacing: 4px; line-height: 1; color: var(--ink);
  }
  .identity__role {
    margin-top: 6px; font-size: 15px; letter-spacing: 12px; line-height: 1; color: var(--ink-soft);
  }
  .contact-list {
    position: absolute; left: 66px; top: 196px;
    list-style: none; display: flex; flex-direction: column; gap: 18px;
    font-size: 21px; letter-spacing: 1.5px; text-transform: uppercase;
  }
  .contact-list li { display: flex; align-items: center; gap: 12px; line-height: 1; }
  .contact-list svg { width: 20px; height: 20px; flex: none; }
  .contact-list .divider { margin: 0 12px; }

  /* Logo side */
  .card--logo {
    background: linear-gradient(160deg, #1b1b1b 0%, var(--card-black) 55%, #000 100%);
    display: flex; flex-direction: column; align-items: center; justify-content: center;
  }
  .brand__name {
    font-size: 84px; letter-spacing: 2px; color: var(--silver); line-height: 1;
  }
  .brand__tagline {
    margin-top: 22px; font-size: 22px; letter-spacing: 6px; color: var(--silver-dim);
    display: flex; align-items: center; gap: 16px; line-height: 1;
  }
  .brand__tagline .sep {
    width: 6px; height: 6px; background: var(--silver-dim); border-radius: 50%;
  }
</style>
</head>
<body>

  <section class="card card--contact" aria-label="Contact side">
    <div class="identity">
      <div class="identity__first">Lisel</div>
      <div class="identity__last">PARDOE</div>
      <div class="identity__role">ARTIST</div>
    </div>
    <ul class="contact-list">
      <li>
        <svg viewBox="0 0 24 24" aria-hidden="true"><path d="M3 12 L12 4 L21 12 H18 V20 H14 V15 H10 V20 H6 V12 Z" fill="currentColor"/></svg>
        118 Coldwell Street, Harlow Park, Vic 3162
      </li>
      <li>
        <svg viewBox="0 0 24 24" aria-hidden="true"><path d="M6 3 L9 3 L11 8 L8.5 10 C9.5 12.5 11.5 14.5 14 15.5 L16 13 L21 15 V18 C21 19.5 20 21 18 21 C10 20.5 3.5 14 3 6 C3 4 4.5 3 6 3 Z" fill="currentColor"/></svg>
        0412 978 205<span class="divider">|</span>03 9187 2604
      </li>
      <li>
        <svg viewBox="0 0 24 24" aria-hidden="true"><rect x="2.5" y="5.5" width="19" height="13" fill="currentColor"/><path d="M3 6 L12 13 L21 6" fill="none" stroke="#fbfbf9" stroke-width="1.5"/></svg>
        lisel@liselpardoe.com
      </li>
      <li>
        <svg viewBox="0 0 24 24" aria-hidden="true"><circle cx="12" cy="12" r="9" fill="none" stroke="currentColor" stroke-width="2"/><ellipse cx="12" cy="12" rx="4" ry="9" fill="none" stroke="currentColor" stroke-width="1.5"/><path d="M3 12 H21 M5 7.5 H19 M5 16.5 H19" stroke="currentColor" stroke-width="1.5"/></svg>
        www.liselsnook.com.au
      </li>
    </ul>
  </section>

  <section class="card card--logo" aria-label="Logo side">
    <div class="brand__name">Lisel's Nook</div>
    <div class="brand__tagline">
      <span>STUDIO</span><span class="sep"></span><span>CAFE</span><span class="sep"></span><span>GALLERY</span>
    </div>
  </section>

</body>
</html>
```